Chiro Card
Bright Path Chiropractic & Wellness
Project: Chiro Card
Chiro Card -
Creative Brief
Simple
Marcus Hale
Chiropractor
812 Orvale Ave, Suite K Corbin Falls, Tx. 78245
corbinfallsspine@mailvane.com
www.corbinfallsspine.com
Please do not include my email address on the business card.

```html
<!DOCTYPE html>
<html lang="en">
<head>
<meta charset="utf-8">
<title>Bright Path Chiropractic &amp; Wellness – Business Cards</title>
<link href="https://fonts.googleapis.com/css2?family=Cinzel:wght@500;600&family=Arimo:wght@400;700&display=swap" rel="stylesheet">
<style>
  :root {
    --green: #3f9e3a;
    --green-light: #8cc63f;
    --green-dark: #1f7f3a;
    --blue: #2b5aa8;
    --blue-dark: #1d3f84;
    --ink: #3a3a3a;
    --white: #ffffff;
    --stage: #eceeea;
    --paper-grey: #e4e7ea;
  }
  * { margin: 0; padding: 0; box-sizing: border-box; }
  html, body { width: 1200px; height: 802px; overflow: hidden; }
  body { background: var(--stage); position: relative; font-family: "Arimo", Arial, sans-serif; }

  .card {
    position: absolute;
    width: 440px;
    height: 252px;
    border-radius: 14px;
    overflow: hidden;
    box-shadow: 0 6px 16px rgba(0,0,0,.18);
  }

  /* Front card */
  .card--front { left: 165px; top: 165px; background: var(--white); }
  .card--front .waves { position: absolute; left: 0; top: 0; width: 100%; height: 100%; }
  .brand { position: absolute; left: 22px; top: 28px; display: flex; align-items: center; gap: 10px; }
  .brand__mark { width: 32px; height: 32px; background: var(--green); border-radius: 4px; }
  .brand__name { font-family: "Cinzel", Georgia, serif; font-weight: 600; font-size: 32px; color: var(--green); line-height: 1; letter-spacing: .5px; }
  .brand__tag { position: absolute; left: 64px; top: 68px; font-family: "Cinzel", Georgia, serif; font-weight: 600; font-size: 13px; color: var(--blue); letter-spacing: .4px; }
  .person { position: absolute; left: 24px; top: 126px; }
  .person__name { font-weight: 700; font-size: 14px; color: var(--green-dark); }
  .person__role { font-size: 10px; color: var(--ink); margin-top: 2px; }
  .contact { position: absolute; right: 18px; top: 104px; text-align: right; font-size: 9.5px; line-height: 1.45; color: var(--ink); }

  /* Green back card */
  .card--back-green {
    left: 608px; top: 120px;
    background: linear-gradient(160deg, var(--green-light) 0%, var(--green) 45%, var(--green-dark) 100%);
  }
  .decor-square { position: absolute; border-radius: 14px; }
  .card--back-green .decor-square { left: 34px; top: 56px; width: 124px; height: 124px; background: rgba(255,255,255,.16); }
  .back-brand { position: absolute; right: 22px; text-align: right; }
  .back-brand__name { font-family: "Cinzel", Georgia, serif; font-weight: 600; font-size: 32px; line-height: 1; }
  .back-brand__url { font-size: 10px; letter-spacing: 1.2px; margin-top: 4px; }
  .card--back-green .back-brand { bottom: 26px; color: var(--white); }

  /* Light back card */
  .card--back-light {
    left: 370px; top: 400px;
    background: linear-gradient(90deg, var(--paper-grey) 0%, var(--white) 45%, var(--white) 100%);
  }
  .card--back-light .decor-square { left: 24px; top: 38px; width: 116px; height: 144px; background: linear-gradient(180deg, #c9d8ea, #e8eef5); opacity: .8; }
  .card--back-light .back-brand { bottom: 26px; }
  .card--back-light .back-brand__name { color: var(--green-dark); }
  .card--back-light .back-brand__url { color: var(--green-dark); }
</style>
</head>
<body>

  <section class="card card--back-green">
    <div class="decor-square"></div>
    <div class="back-brand">
      <div class="back-brand__name">BRIGHT PATH</div>
      <div class="back-brand__url">www.corbinfallsspine.com</div>
    </div>
  </section>

  <section class="card card--front">
    <svg class="waves" viewBox="0 0 440 252" preserveAspectRatio="none" aria-hidden="true">
      <defs>
        <linearGradient id="bandGreen" x1="0" y1="0" x2="1" y2="0">
          <stop offset="0" stop-color="#8cc63f"/>
          <stop offset="1" stop-color="#2f9440"/>
        </linearGradient>
        <linearGradient id="bandBlue" x1="0" y1="0" x2="1" y2="0">
          <stop offset="0" stop-color="#2b5aa8"/>
          <stop offset="1" stop-color="#1d3f84"/>
        </linearGradient>
      </defs>
      <path d="M0 178 C 120 198, 260 175, 440 156 L 440 164 C 260 186, 130 212, 0 192 Z" fill="url(#bandBlue)"/>
      <path d="M0 210 C 140 224, 280 190, 440 172 L 440 252 L 0 252 Z" fill="url(#bandGreen)"/>
    </svg>
    <div class="brand">
      <div class="brand__mark"></div>
      <div class="brand__name">BRIGHT PATH</div>
    </div>
    <div class="brand__tag">CHIROPRACTIC &amp; WELLNESS</div>
    <div class="person">
      <div class="person__name">Marcus Hale</div>
      <div class="person__role">Chiropractor</div>
    </div>
    <div class="contact">
      812 Orvale Ave, Suite K<br>
      Corbin Falls, Tx. 78245<br>
      Phone: (830) 555-0142
    </div>
  </section>

  <section class="card card--back-light">
    <div class="decor-square"></div>
    <div class="back-brand">
      <div class="back-brand__name">BRIGHT PATH</div>
      <div class="back-brand__url">www.corbinfallsspine.com</div>
    </div>
  </section>

</body>
</html>
```